Zorvan Voltline Services requires a modern & sharp looking sign.

We need a sign to be designed for a local soccer club ground where advertising will take place. Text needs to be limited with only the basic information such as the logo/company name, website and mobile number. The EC40923 number must be placed somewhere in the sign.

The design should be similar to the flyer design attached, but in a more plain looking version.

Signage dimensions are 2050mm Wide x 900mm High.

Industry/Entity Type

Electrician

Requirements
Must have
• Logo/Company Name
• EC Number
• Website (www.zorvanvoltline.com.au)
• Phone Number
• - SAME COLOR SCHEME AS THE LOGO
• - SAME LIGHTNING BOLT TO THE RIGHT OF THE SIGN (REFER TO FLYER)
Should not have
• NO PICTURES

```html
<!DOCTYPE html>
<html lang="en">
<head>
<meta charset="utf-8">
<title>Zorvan Voltline Services – Ground Sign</title>
<link rel="stylesheet" href="https://fonts.googleapis.com/css2?family=Exo+2:wght@500;600;700;800&display=swap">
<style>
  :root {
    --blue: #0a14f0;
    --grey-mid: #a3a3a3;
    --grey-light: #dcdcdc;
    --white: #ffffff;
    --backdrop-centre: #b4b4b4;
    --backdrop-edge: #555555;
  }
  * { margin: 0; padding: 0; box-sizing: border-box; }
  html, body { width: 1200px; height: 1125px; overflow: hidden; }
  body {
    background: radial-gradient(ellipse at 50% 50%, var(--backdrop-centre) 0%, #8a8a8a 45%, var(--backdrop-edge) 100%);
    position: relative;
    font-family: "Exo 2", sans-serif;
  }
  .sign {
    position: absolute;
    left: 170px;
    width: 860px;
    height: 376px;
    overflow: hidden;
    background: linear-gradient(160deg, var(--white) 0%, #f4f4f4 50%, #e2e2e2 100%);
    box-shadow: 8px 10px 14px rgba(0,0,0,0.35);
  }
  .sign--with-mark { top: 130px; }
  .sign--wordmark { top: 618px; }

  .sign__decor { position: absolute; inset: 0; }

  .brand { position: absolute; color: var(--blue); line-height: 1; white-space: nowrap; }
  .brand__main { display: block; font-weight: 800; letter-spacing: 2px; }
  .brand__sub { display: block; font-weight: 600; }

  .sign--with-mark .brand { left: 162px; top: 38px; }
  .sign--with-mark .brand__main { font-size: 100px; }
  .sign--with-mark .brand__sub { font-size: 30px; margin-top: 12px; letter-spacing: 6px; }

  .sign--wordmark .brand { left: 34px; top: 22px; }
  .sign--wordmark .brand__main { font-size: 132px; letter-spacing: 4px; }
  .sign--wordmark .brand__sub { font-size: 38px; margin-top: 10px; letter-spacing: 8px; }

  .phone {
    position: absolute;
    left: 30px;
    font-weight: 700;
    font-size: 42px;
    color: var(--white);
    letter-spacing: 1px;
    line-height: 1;
    white-space: nowrap;
  }
  .sign--with-mark .phone { top: 220px; }
  .sign--wordmark .phone { top: 245px; }

  .website {
    position: absolute;
    left: 30px;
    font-weight: 800;
    font-size: 34px;
    color: var(--blue);
    letter-spacing: -0.8px;
    line-height: 1;
    white-space: nowrap;
  }
  .sign--with-mark .website { top: 314px; }
  .sign--wordmark .website { top: 322px; }

  .licence {
    position: absolute;
    right: 26px;
    bottom: 24px;
    font-weight: 800;
    font-size: 26px;
    color: var(--white);
    line-height: 1;
  }
</style>
</head>
<body>

  <section class="sign sign--with-mark" aria-label="Sign layout with brand circle">
    <svg class="sign__decor" width="860" height="376" viewBox="0 0 860 376" aria-hidden="true">
      <circle cx="662" cy="190" r="206" fill="var(--grey-light)"/>
      <circle cx="662" cy="190" r="190" fill="var(--grey-mid)"/>
      <circle cx="84" cy="94" r="58" fill="none" stroke="var(--blue)" stroke-width="10"/>
      <polygon points="0,207 448,207 462,275 0,275" fill="var(--blue)"/>
    </svg>
    <div class="brand">
      <span class="brand__main">ZORVAN</span>
      <span class="brand__sub">VOLTLINE SERVICES</span>
    </div>
    <p class="phone">Tel 0491 570 338</p>
    <p class="website">www.zorvanvoltline.com.au</p>
    <p class="licence">EC40923</p>
  </section>

  <section class="sign sign--wordmark" aria-label="Sign layout with large name">
    <svg class="sign__decor" width="860" height="376" viewBox="0 0 860 376" aria-hidden="true">
      <circle cx="662" cy="190" r="206" fill="var(--grey-light)"/>
      <circle cx="662" cy="190" r="190" fill="var(--grey-mid)"/>
      <polygon points="0,232 452,232 470,300 0,300" fill="var(--blue)"/>
    </svg>
    <div class="brand">
      <span class="brand__main">ZORVAN</span>
      <span class="brand__sub">VOLTLINE SERVICES</span>
    </div>
    <p class="phone">Tel 0491 570 338</p>
    <p class="website">www.zorvanvoltline.com.au</p>
    <p class="licence">EC40923</p>
  </section>

</body>
</html>
```